Home Care company needs letter head branding

Home care company needs a letter head which can be used for all documents the company's clients view. We provided in home care for the elderly. We would like to use our company colors (2785A7, 0A4057 and 34A74D) and should not be too large as we will be using it on more than just a letter head but all documents our clients sign / receive.
Target Market(s)
Professional business
Industry/Entity Type
Health Care
Requirements
Must have
- corporate brand colors

```html
<!DOCTYPE html>
<html lang="en">
<head>
<meta charset="utf-8">
<title>Ashgrove Care Letterhead</title>
<link href="https://fonts.googleapis.com/css2?family=Lora:wght@600&display=swap" rel="stylesheet">
<style>
  :root {
    --brand-green: #41ac56;
    --accent-lime: #acd043;
    --brand-blue: #2785a7;
    --paper: #ffffff;
  }
  html, body {
    margin: 0;
    padding: 0;
    width: 928px;
    height: 1200px;
    overflow: hidden;
    background: var(--paper);
  }
  .letterhead {
    position: relative;
    width: 928px;
    height: 1200px;
    background: var(--paper);
    overflow: hidden;
  }
  .letterhead__waves {
    position: absolute;
    inset: 0;
    width: 928px;
    height: 1200px;
  }
  .wave--lime { fill: var(--accent-lime); }
  .wave--green { fill: var(--brand-green); }
  .brand__mark {
    fill: var(--paper);
    stroke: var(--brand-blue);
    stroke-width: 7;
  }
  .brand__name {
    position: absolute;
    left: 202px;
    top: 30px;
    margin: 0;
    font-family: "Lora", Georgia, serif;
    font-weight: 600;
    font-size: 50px;
    line-height: 1;
    letter-spacing: -0.5px;
    color: var(--paper);
    white-space: nowrap;
  }
</style>
</head>
<body>
  <div class="letterhead">
    <svg class="letterhead__waves" viewBox="0 0 1100 1423" preserveAspectRatio="none" aria-hidden="true">
      <path class="wave--lime" d="M0,0 H882 C800,100 650,172 470,172 C330,172 180,122 0,90 Z"/>
      <path class="wave--green" d="M0,0 H872 C782,86 640,150 470,150 C330,150 180,96 0,56 Z"/>
      <path class="wave--lime" d="M578,1423 C680,1375 780,1355 860,1356 C950,1357 1040,1378 1100,1395 V1423 Z"/>
      <path class="wave--green" d="M612,1423 C700,1392 790,1378 860,1378 C950,1378 1040,1395 1100,1410 V1423 Z"/>
      <circle class="brand__mark" cx="128" cy="105" r="76"/>
    </svg>
    <h1 class="brand__name">Ashgrove Care</h1>
  </div>
</body>
</html>
```